Flyer Vermietung von Partyanlagen
Zielgruppe
Wir sind ein junges Unternehmen, welches Veranstaltungsequipment für private Endkunden zur Miete anbietet. Vor allem sind wir auf die Vermietung von 'Komplettpaketen' spezialisiert, die aus Licht- und Audioequipment für eigene Feierlichkeiten bestehen.
Aufgabenstellung
Wir benötigen ein auffälliges und modernes Design, was gerne mit Designelementen geschmückt werden darf. Im Vordergrund muss unser Angebot stehen ( Vermietung professioneller Partyanlagen zu günstigen Preisen). Die Maße können innerhalb der DIN-Vorgaben frei gewählt werden ( DIN- A5/A6/Lang).
Der Leser des Flyers soll angeregt werden, sich für seine Feierlichkeit eine Komplettanlage von uns zu mieten, da diese professionell, günstig und einfach im Aufbau sind.
Ein Beispiel der am häufigsten vermieteten Anlage, sowie unsere Leistungen finden Sie im folgenden Text, der von Ihnen verwendet werden sollte, gerne angepasst werden darf und soll zu Ihrer Information dient.
Unser Angebot :
Party Komplettpaket aus Licht & Ton für deine Party.
Bestehend aus :
2x Tonfels Audio Aktiv Lautsprecher ( 1000 Watt Class D)
1x 15' Subwoofer (1200 Watt Class D)
1x Lichtanlage mit 4 Scheinwerfern
1x raumfüllender LED-Effekt
Mischpult zum Anschluss von Audioquellen ( Laptop o.Ä.)
RBQ Funkmikrofon
Nebelmaschine
- alle nötigen Stative & Kabel
für nur 90 Euro komplett
inklusive Lieferung in Werne ( geringe Aufpreis in der Umgebung)
zu ergänzen zum Beispiel mit :
- Subwoofern
- Movingheads, weiteren Lichteffekten etc.
- Equipmentverleih
- Individuelle Mietanlagen
- Licht-/Tontechnik
- Traversensysteme
- Technischer Support
- Anlieferung & Aufbau
- Dry Hire
Weitere Angaben, die auf dem Flyer erscheinen sollen:
Website : www.7k-eventwerk.de
(Private Daten würden wir später weitergeben)
Unser Logo wird in einem anderen Projekt ausgeschrieben - dafür bitte etwas Platz lassen ( bzw. von dem selben Designer kann es auch nicht schaden ;-) )
Die weiteren Bilder sind leider qualitativ nicht sehr hochwertig ( da jeweils von Kunden) - können aber verwendet werden und dienen ebenfalls Ihrer Veranschaulich..

```html
<!DOCTYPE html>
<html lang="de">
<head>
<meta charset="utf-8">
<title>Flyer – Vermietung von Partyanlagen</title>
<link rel="stylesheet" href="https://fonts.googleapis.com/css2?family=Lobster&family=Arimo:ital,wght@0,400;0,700;1,700&display=swap">
<style>
  :root {
    --stage: #d4d4d4;
    --ink: #0c0c0c;
    --smoke: #3a3a3a;
    --white: #ffffff;
    --gold: #e59a12;
    --magenta: #e5007e;
  }
  * { box-sizing: border-box; margin: 0; padding: 0; }
  html, body { width: 1200px; height: 839px; overflow: hidden; }
  body {
    background: radial-gradient(circle at 50% 45%, #e6e6e6, var(--stage) 70%, #b9b9b9);
    font-family: "Arimo", Arial, sans-serif;
    position: relative;
  }
  .flyer {
    position: absolute; left: 317px; top: 20px;
    width: 566px; height: 800px;
    background: var(--ink);
    overflow: hidden;
    box-shadow: 0 8px 30px rgba(0,0,0,.35);
  }
  .hero-photo {
    position: absolute; left: 0; top: 0; width: 100%; height: 470px;
    background: linear-gradient(180deg, #2a2a2a 0%, #4a4a4a 30%, #3b3b3b 60%, #111 100%);
  }
  .title-band {
    position: absolute; left: 0; top: 30px; width: 100%; height: 170px;
    background: rgba(0,0,0,.55);
  }
  .headline {
    position: absolute; left: 36px; top: 36px;
    font-family: "Lobster", cursive;
    line-height: 1;
  }
  .headline .lead { color: var(--white); font-size: 30px; }
  .headline .accent { color: var(--gold); font-size: 38px; }
  .headline .big { display: block; color: var(--gold); font-size: 48px; margin-top: 4px; }
  .subline {
    position: absolute; left: 36px; top: 156px;
    color: var(--white); font-weight: 700; font-size: 20px;
  }
  .event-photo {
    position: absolute; top: 222px; width: 126px; height: 126px;
    border-radius: 50%;
    border: 3px solid rgba(255,255,255,.8);
    box-shadow: 0 0 18px 6px rgba(255,255,255,.35);
  }
  .event-photo.one { left: 50px; background: radial-gradient(circle at 40% 35%, #e6a0f0, #8a3aa8 60%, #2d1a3a); }
  .event-photo.two { left: 220px; background: radial-gradient(circle at 50% 30%, #ff5a6e, #b3102e 55%, #2a0510); }
  .event-photo.three { left: 390px; background: radial-gradient(circle at 50% 45%, #c6a0ff, #7b48c8 55%, #2b1f40); }
  .offer-banner { position: absolute; left: 0; top: 385px; width: 566px; height: 92px; }
  .offer-title {
    position: absolute; left: 48px; top: 402px;
    color: var(--magenta); font-weight: 700; font-style: italic; font-size: 25px; line-height: 1.2;
  }
  .offer-sub {
    position: absolute; left: 48px; top: 438px;
    color: var(--magenta); font-weight: 700; font-style: italic; font-size: 13px; line-height: 1.2;
  }
  .gear-photo {
    position: absolute; left: 300px; top: 345px; width: 266px; height: 255px;
    background: radial-gradient(ellipse at 65% 55%, #3c3c3c, #1a1a1a 60%, transparent 75%);
  }
  .package {
    position: absolute; left: 50px; top: 484px; width: 330px; color: var(--white);
    font-weight: 700;
  }
  .package h2 { font-size: 16px; line-height: 1.15; text-decoration: underline; margin-bottom: 4px; }
  .package ul { list-style: none; font-size: 13.5px; line-height: 1.24; }
  .package li::before { content: "» "; font-size: 11px; }
  .package li .cont { display: block; padding-left: 12px; }
  .price-tag { position: absolute; left: 405px; top: 560px; width: 150px; height: 78px; }
  .price-text {
    position: absolute; left: 425px; top: 570px; width: 120px;
    color: var(--magenta); font-weight: 700; font-style: italic;
    font-size: 15px; line-height: 1.15; text-align: center;
  }
  .delivery {
    position: absolute; left: 50px; top: 681px; color: var(--white); font-weight: 700;
  }
  .delivery p { font-size: 11px; line-height: 1.2; }
  .delivery small { display: block; font-size: 8px; line-height: 1.2; }
  .more-info {
    position: absolute; left: 40px; top: 709px;
    color: var(--white); font-weight: 700; font-size: 22px; line-height: 1.15;
  }
  .contact {
    position: absolute; left: 0; top: 745px; width: 100%; height: 55px;
    background: var(--white); color: var(--ink);
    text-align: center; font-weight: 700;
    padding-top: 6px;
  }
  .contact h3 { font-size: 12px; line-height: 1.2; }
  .contact p { font-size: 10px; line-height: 1.35; }
</style>
</head>
<body>
  <article class="flyer">
    <div class="hero-photo" role="img" aria-label="Hintergrundfoto eines Veranstaltungsraums mit Traversen und Lichtnebel"></div>
    <div class="title-band"></div>
    <h1 class="headline">
      <span class="lead">Dein</span> <span class="accent">Party- und</span>
      <span class="big">Veranstaltungsequipment</span>
    </h1>
    <p class="subline">Vermietung professioneller Ton-/Lichtanlagen</p>

    <div class="event-photo one" role="img" aria-label="Foto einer aufgebauten Anlage mit violetter Beleuchtung"></div>
    <div class="event-photo two" role="img" aria-label="Foto einer Party mit roter Bühnenbeleuchtung"></div>
    <div class="event-photo three" role="img" aria-label="Foto eines Saals mit Traverse und lila Licht"></div>

    <div class="gear-photo" role="img" aria-label="Produktfoto: zwei Aktivlautsprecher auf Stativen, Subwoofer und Lichtanlage mit vier Scheinwerfern"></div>

    <svg class="offer-banner" viewBox="0 0 566 92" aria-hidden="true">
      <polygon points="0,14 400,0 375,92 0,92" fill="#ffffff"/>
    </svg>
    <p class="offer-title">Unser Angebot :</p>
    <p class="offer-sub">Party Komplettpaket aus Licht &amp; Ton für deine Party.</p>

    <section class="package">
      <h2>Bestehend aus:</h2>
      <ul>
        <li>2x Tonfels Audio Aktiv Lautsprecher<span class="cont">(1000 Watt Class D)</span></li>
        <li>1x 15‘ Subwoofer (1200 Watt Class D)</li>
        <li>1x Lichtanlage mit 4 Scheinwerfern</li>
        <li>1x raumfüllender LED-Effekt</li>
        <li>Mischpult zum Anschluss von<span class="cont">Audioquellen ( Laptop o.Ä.)</span></li>
        <li>RBQ Funkmikrofon</li>
        <li>Nebelmaschine</li>
        <li>alle nötigen Stative &amp; Kabel</li>
      </ul>
    </section>

    <svg class="price-tag" viewBox="0 0 150 78" aria-hidden="true">
      <polygon points="18,6 150,0 150,72 0,78" fill="#ffffff"/>
    </svg>
    <p class="price-text">Komplett<br>ab 90 Euro<br>zu mieten!</p>

    <div class="delivery">
      <p>Inklusive Gratislieferung innerhalb Werne.</p>
      <small>(Lieferung ausserhalb von Werne gegen geringe Liefergebühr möglich.)</small>
    </div>

    <p class="more-info">... mehr Infos unter www.7k-eventwerk.de</p>

    <footer class="contact">
      <h3>Kontakt:</h3>
      <p>Tobias Kleinert | 7K-Eventwerk | Lindenallee 8 | 59300 Werne | Telefon: 0157/12 48 90 36</p>
      <p>www.7k-eventwerk.de | E-Mail: info@7k-eventwerk.de</p>
    </footer>
  </article>
</body>
</html>
```